ebook cover for The Heron & The Badger (Squawk!)

We would like an ebook cover for a post Ph.D. on Animal Totems book called The Heron and The Badger. It is about human relationships and dating. Author is Marla Quenby Ph.D.
I am thinking perhaps just typographic with a fancy custom italicized or handwriting kind of font that fills the whole page, or a picture that doesn't belittle the fairytale of love. Something cosmic.
The subtitle to guide people, small, is "on dating"

```html
<!DOCTYPE html>
<html lang="en">
<head>
<meta charset="utf-8">
<title>The Heron and The Badger — On Dating</title>
<link rel="stylesheet" href="https://fonts.googleapis.com/css2?family=Kaushan+Script&family=Montserrat:wght@500&family=Tinos&display=swap">
<style>
  :root {
    --page-bg: #dcdcdc;
    --sky-black: #04060a;
    --sky-night: #0d1520;
    --sky-blue: #2a3a55;
    --haze-violet: #8c7295;
    --haze-pink: #d9b7cf;
    --horizon-glow: #fff3e6;
    --field-gold: #a8923a;
    --field-olive: #6f6126;
    --field-earth: #3b2312;
    --ink-white: #ffffff;
  }

  * { box-sizing: border-box; margin: 0; padding: 0; }

  html, body {
    width: 1200px;
    height: 800px;
    overflow: hidden;
    background: var(--page-bg);
  }

  .canvas {
    position: relative;
    width: 1200px;
    height: 800px;
    display: flex;
    align-items: center;
    justify-content: center;
  }

  .cover {
    position: relative;
    width: 456px;
    height: 740px;
    overflow: hidden;
    color: var(--ink-white);
  }

  .cover-art {
    position: absolute;
    inset: 0;
    background:
      radial-gradient(ellipse 45% 6% at 48% 66%, var(--horizon-glow) 0%, rgba(255,236,220,0.6) 40%, rgba(255,236,220,0) 100%),
      radial-gradient(ellipse 70% 14% at 45% 62%, rgba(217,183,207,0.75) 0%, rgba(140,114,149,0.35) 55%, rgba(140,114,149,0) 100%),
      radial-gradient(ellipse 30% 12% at 80% 76%, rgba(255,230,120,0.45) 0%, rgba(255,230,120,0) 100%),
      linear-gradient(180deg,
        var(--sky-black) 0%,
        var(--sky-black) 28%,
        var(--sky-night) 38%,
        var(--sky-blue) 52%,
        var(--haze-violet) 60%,
        var(--haze-pink) 65%,
        var(--field-gold) 68%,
        var(--field-olive) 80%,
        var(--field-earth) 100%);
  }

  .title {
    position: absolute;
    left: 0;
    right: 0;
    top: 30px;
    font-family: "Kaushan Script", cursive;
    font-weight: 400;
    line-height: 1;
    text-align: center;
  }

  .title-line { display: block; }

  .title-small {
    font-size: 58px;
  }

  .title-big {
    font-size: 104px;
  }

  .title .the-first  { margin-left: 80px; }
  .title .heron      { margin-top: -14px; margin-left: -10px; }
  .title .and        { font-size: 48px; margin-top: -10px; }
  .title .the-second { margin-top: 2px; }
  .title .badger     { margin-top: -22px; font-size: 96px; }

  .subtitle {
    position: absolute;
    left: 0;
    right: 0;
    top: 430px;
    text-align: center;
    font-family: "Montserrat", sans-serif;
    font-weight: 500;
    font-size: 22px;
    letter-spacing: 0.16em;
  }

  .author {
    position: absolute;
    left: 0;
    right: 0;
    bottom: 22px;
    text-align: center;
    font-family: "Tinos", serif;
    font-size: 27px;
    letter-spacing: 0.2em;
  }
</style>
</head>
<body>
  <main class="canvas">
    <article class="cover">
      <div class="cover-art" role="img" aria-label="Cosmic night sky with scattered stars fading into a glowing sunset over a grassy meadow, where one person lies in the grass and another stands catching falling stars beside a picnic basket"></div>

      <h1 class="title">
        <span class="title-line title-small the-first">The</span>
        <span class="title-line title-big heron">Heron</span>
        <span class="title-line title-small and">and</span>
        <span class="title-line title-small the-second">The</span>
        <span class="title-line title-big badger">Badger</span>
      </h1>

      <p class="subtitle">ON DATING</p>

      <p class="author">Marla Quenby Ph.D.</p>
    </article>
  </main>
</body>
</html>
```